Awesome Valdren Business Card Project

We would like a double-sided business card. We have a primary PMS color of PMS 1505 and a secondary color of PMS 1495. I would like to include our logo, the secondary S logo, and the QTALX logo on the business card. We will want a spot for the following information.
Marisa Colton
Valdren
Address: 4318 N Fable Avenue Oak Terrace, IL 60291
Email: mcolton@valdren.example
Phone: 312-555-0148
Mobile: (414) 555-0193
Website: www.valdren.example
Contact Information for Business Card
Marisa Colton Valdren Address: 4318 N Fable Avenue Oak Terrace, IL 60291 Email: mcolton@valdren.example Phone: 312-555-0148 Mobile: (414) 555-0193 Website: www.valdren.example

```html
<!DOCTYPE html>
<html lang="en">
<head>
<meta charset="utf-8">
<title>Valdren Business Card</title>
<link rel="stylesheet" href="https://fonts.googleapis.com/css2?family=Open+Sans:wght@400;700&display=swap">
<style>
  :root {
    --stage: #3a3d42;
    --card: #231f20;
    --orange: #ff7300;
    --orange-light: #ff9933;
    --mark-dark: #2f2c2d;
    --mark-darker: #282425;
    --text: #f2f2f2;
    --muted: #8a8a8a;
  }
  * { box-sizing: border-box; margin: 0; padding: 0; }
  html, body {
    width: 1200px; height: 952px; overflow: hidden;
    background: var(--stage);
    font-family: "Open Sans", Arial, sans-serif;
  }
  .sheet {
    width: 1200px; height: 952px;
    display: flex; flex-direction: column; align-items: center; justify-content: center;
    gap: 24px;
  }
  .card {
    position: relative;
    width: 760px; height: 434px;
    background: var(--card);
    overflow: hidden;
    box-shadow: 0 10px 30px rgba(0,0,0,.35);
  }
  .wordmark {
    position: absolute;
    color: var(--orange);
    font-weight: 400;
    letter-spacing: 1px;
    line-height: 1;
  }
  .card-front .wordmark { left: 250px; top: 48px; font-size: 64px; }
  .card-back .wordmark { left: 70px; top: 140px; font-size: 80px; }

  .brand-mark-area { position: absolute; }
  .card-front .brand-mark-area {
    left: 330px; top: 260px; width: 250px; height: 174px;
    border-radius: 60px 60px 0 0;
    background: linear-gradient(135deg, var(--orange) 0%, var(--orange-light) 100%);
  }
  .card-back .brand-mark-area {
    left: 400px; top: 60px; width: 320px; height: 374px;
    border-radius: 120px 120px 0 0;
    background: linear-gradient(160deg, var(--mark-dark) 0%, var(--mark-darker) 100%);
  }

  .contact-list {
    position: absolute; left: 44px; top: 160px;
    list-style: none;
    color: var(--text);
    font-size: 15px; line-height: 1.25;
  }
  .contact-list li { display: flex; align-items: flex-start; gap: 10px; margin-bottom: 8px; }
  .contact-icon {
    flex: none; width: 20px; height: 20px; border-radius: 3px;
    background: var(--orange-light);
    display: flex; align-items: center; justify-content: center;
  }
  .contact-icon svg { width: 13px; height: 13px; fill: none; stroke: #fff; stroke-width: 2; stroke-linecap: round; stroke-linejoin: round; }

  .cert-badge {
    position: absolute; left: 200px; top: 350px;
    width: 96px; height: 50px;
    border: 2px solid var(--muted); border-radius: 6px;
    background: #2e2a2b;
  }

  .holder {
    position: absolute; right: 44px; top: 170px;
    text-align: right;
  }
  .holder-name { color: var(--orange); font-weight: 700; font-size: 32px; line-height: 1.1; }
  .holder-rule { width: 120px; height: 1px; background: var(--orange); margin: 10px 0 6px auto; }
  .holder-company { color: var(--text); font-size: 17px; }
</style>
</head>
<body>
<main class="sheet">
  <section class="card card-front" aria-label="Business card front">
    <div class="wordmark">Valdren</div>

    <ul class="contact-list">
      <li>
        <span class="contact-icon"><svg viewBox="0 0 16 16"><path d="M8 15s5-5 5-8.5A5 5 0 0 0 3 6.5C3 10 8 15 8 15z"/><circle cx="8" cy="6.5" r="1.6"/></svg></span>
        <span>4318 N Fable Avenue<br>Oak Terrace, IL 60291</span>
      </li>
      <li>
        <span class="contact-icon"><svg viewBox="0 0 16 16"><path d="M4 2h3l1 3-2 1a8 8 0 0 0 4 4l1-2 3 1v3a1 1 0 0 1-1 1A11 11 0 0 1 3 3a1 1 0 0 1 1-1z"/></svg></span>
        <span>312-555-0148</span>
      </li>
      <li>
        <span class="contact-icon"><svg viewBox="0 0 16 16"><rect x="4.5" y="1.5" width="7" height="13" rx="1.5"/><path d="M7 12h2"/></svg></span>
        <span>(414) 555-0193</span>
      </li>
      <li>
        <span class="contact-icon"><svg viewBox="0 0 16 16"><rect x="1.5" y="3.5" width="13" height="9" rx="1"/><path d="M2 4l6 5 6-5"/></svg></span>
        <span>mcolton@valdren.example</span>
      </li>
      <li>
        <span class="contact-icon"><svg viewBox="0 0 16 16"><path d="M3 2l10 5-4 1.5L7.5 13z"/></svg></span>
        <span>www.valdren.example</span>
      </li>
    </ul>

    <div class="cert-badge" role="img" aria-label="Certification badge"></div>

    <div class="brand-mark-area" role="img" aria-label="Large orange brand mark"></div>

    <div class="holder">
      <div class="holder-name">Marisa Colton</div>
      <div class="holder-rule"></div>
      <div class="holder-company">Valdren</div>
    </div>
  </section>

  <section class="card card-back" aria-label="Business card back">
    <div class="brand-mark-area" role="img" aria-label="Large faint brand mark"></div>
    <div class="wordmark">Valdren</div>
  </section>
</main>
</body>
</html>
```